Lantern Gathering event flyer

I would like a church event flyer designed. The event is called "LANTERN GATHERING 2018". I am looking for a professional, yet catchy design that uses our brand colors and logo creatively while communicating key information of the event effectively.

1. The logo is attached in two color formats. The designer has the choice to use them as he/she want.

2. The location of the event is: Halvorn Community Center, 53 Tillory Lane, Portland, ME 04917
3. Time and date of event. The designer can organize and format the date and time as he/she pleases.
December 28th, 29th @ 7:00PM
December 30th @ 10:00AM
4. The topic of the event is "Wings of dawn". The designer is free to use this phrase as he/she pleases to create a good composition.
5. Speaker: Prophet Marcus Obileh
6. Contact information: contact@cedarvalefold.org - Telephone number: 207 555 0143

7. I would also like the following three words on the flyer. These words describe the focus of the event: FIRE, REVIVAL, PROPHETIC

```html
<!DOCTYPE html>
<html lang="en">
<head>
<meta charset="utf-8">
<title>Lantern Gathering 2018 Flyer</title>
<link rel="stylesheet" href="https://fonts.googleapis.com/css2?family=Cinzel:wght@400;500;600&display=swap">
<style>
  :root {
    --page: #eeeeec;
    --navy: #0f3560;
    --orange: #f7941d;
    --white: #ffffff;
  }
  html, body {
    margin: 0;
    width: 1200px;
    height: 1200px;
    overflow: hidden;
    background: var(--page);
  }
  .flyer {
    position: absolute;
    left: 197px;
    top: 30px;
    width: 807px;
    height: 1141px;
    box-shadow: 0 2px 10px rgba(0,0,0,0.18);
  }
  .flyer text {
    font-family: "Cinzel", serif;
    text-anchor: middle;
    fill: var(--white);
  }
  .brand-name { font-size: 36px; font-weight: 500; letter-spacing: 1px; }
  .title-line { font-size: 84px; font-weight: 400; }
  .title-year { font-size: 100px; font-weight: 400; }
  .theme { font-size: 44px; font-weight: 600; fill: var(--orange) !important; }
  .focus-words { font-size: 27px; letter-spacing: 1px; }
  .schedule { font-size: 38px; font-weight: 500; }
  .schedule .ord { font-size: 21px; }
  .schedule .at { font-family: "Times New Roman", serif; }
  .speaker-label { font-size: 22px; }
  .speaker-name { font-size: 26px; font-weight: 500; letter-spacing: 0.5px; }
  .venue { font-size: 25px; letter-spacing: 0.5px; }
  .contact-label { font-size: 21px; fill: var(--orange) !important; }
  .contact-line { font-size: 21px; }
</style>
</head>
<body>
<svg class="flyer" viewBox="0 0 807 1141" xmlns="http://www.w3.org/2000/svg">
  <defs>
    <linearGradient id="photoFade" x1="0" y1="0" x2="0" y2="1">
      <stop offset="0" stop-color="#9db3d2"/>
      <stop offset="0.35" stop-color="#7690b8"/>
      <stop offset="0.65" stop-color="#4f6f9c"/>
      <stop offset="1" stop-color="#0f3560"/>
    </linearGradient>
    <radialGradient id="domeGlow" cx="0.5" cy="0.32" r="0.45">
      <stop offset="0" stop-color="#d4deec" stop-opacity="0.7"/>
      <stop offset="1" stop-color="#d4deec" stop-opacity="0"/>
    </radialGradient>
  </defs>

  <rect class="flyer-base" x="0" y="0" width="807" height="1141" fill="var(--navy)"/>

  <g role="img" aria-label="Photograph of an ornate cathedral interior looking up toward the domed ceiling, tinted blue">
    <rect x="0" y="0" width="807" height="870" fill="url(#photoFade)"/>
    <rect x="0" y="0" width="807" height="870" fill="url(#domeGlow)"/>
  </g>

  <!-- brand tab -->
  <path class="brand-tab" d="M289 0 H519 V162 A115 115 0 0 1 404 277 A115 115 0 0 1 289 162 Z" fill="var(--navy)"/>
  <text class="brand-name" x="404" y="150">CEDARVALE</text>

  <!-- title frame -->
  <rect x="104" y="290" width="599" height="388" fill="none" stroke="var(--orange)" stroke-width="2"/>
  <rect x="105" y="635" width="597" height="42" fill="var(--navy)"/>
  <line x1="104" y1="635" x2="703" y2="635" stroke="var(--orange)" stroke-width="2"/>

  <text class="title-line" x="404" y="390">LANTERN</text>
  <text class="title-line" x="404" y="476">GATHERING</text>
  <text class="title-year" x="404" y="564">2018</text>
  <text class="theme" x="404" y="612">Wings of dawn</text>
  <text class="focus-words" x="404" y="666">FIRE, REVIVAL, PROPHETIC</text>

  <!-- schedule -->
  <text class="schedule" x="404" y="769">December 28<tspan class="ord" dy="-14">TH</tspan><tspan dy="14">, 29</tspan><tspan class="ord" dy="-14">TH</tspan><tspan dy="14"> </tspan><tspan class="at">@</tspan><tspan> 7:00PM</tspan></text>
  <line x1="94" y1="782" x2="700" y2="782" stroke="var(--white)" stroke-width="1"/>
  <text class="schedule" x="404" y="825">December 30<tspan class="ord" dy="-14">TH</tspan><tspan dy="14"> </tspan><tspan class="at">@</tspan><tspan> 10:00AM</tspan></text>

  <!-- speaker -->
  <rect x="225" y="861" width="357" height="25" fill="var(--orange)"/>
  <rect x="226" y="861" width="355" height="64" fill="none" stroke="var(--orange)" stroke-width="1.5"/>
  <text class="speaker-label" x="404" y="881">Speaker:</text>
  <text class="speaker-name" x="404" y="915">Prophet Marcus Obileh</text>

  <!-- venue -->
  <text class="venue" x="404" y="974">Halvorn Community Center,</text>
  <text class="venue" x="404" y="1001">53 Tillory Lane, Portland, ME 04917</text>

  <!-- contact -->
  <line x1="245" y1="1038" x2="557" y2="1038" stroke="var(--white)" stroke-width="1"/>
  <text class="contact-label" x="404" y="1069">Contact information:</text>
  <text class="contact-line" x="404" y="1094">contact@cedarvalefold.org   |   Tel No: 207 555 0143</text>
</svg>
</body>
</html>
```